Design of a roll up banner (for HR recruiting events in the field of IT & Consulting)

We need a design for a roll up banner which can be used when attending HR recruiting events / recruiting fairs. Our company is specialized in Performance Engineering and is offering our customers consulting services in the field of load & performance testing as well as application performance monitoring.
We would love to address potential new employees with a roll up banner stating our working benefits such as (text in German as we are attending German events):
* bis zu 100% Homeoffice möglich
* Essenszuschuss
* Öffi-Ticket
* Weiterbildungen
* Gleitzeit und vieles mehr
Maybe a link to our career website would be suitable on the roll up banner (https://www.velmarok-it.com/de/career/joboffers/)?
Of course our logo should be attached to the banner. The color values of the dark blue color are:
RGB 11 – 79 – 143
HEX #0B4F8F
Pantone 541 C
CMYK 92 - 45 - 0 - 44 (cyan - magenta - yellow - key)
Last, but not least the design should have the measures required for this exact roll up banner system:
https://www.druckzelbara.at/p/rollup-system-exklusiv-100x215cm?depvar_index_setparent=%3cLR41240%3e%3cLR41240.X17.SI2%3e&depvar_index_set_1=%3cZXXXXX3D%3e%3cZXXXXX3DD00%3e&depvar_index_set_2=%3cZR4XX00Y%3e%3cZR4XX00YY45%3e
We are looking forward to receiving your design proposals!

```html
<!DOCTYPE html>
<html lang="de">
<head>
<meta charset="UTF-8">
<title>Velmarok – Roll-up Recruiting</title>
<link rel="stylesheet" href="https://fonts.googleapis.com/css2?family=Montserrat:wght@500;700;800&display=swap">
<style>
  :root {
    --page-bg: #eef1f5;
    --brand-dark: #0B4F8F;
    --navy: #0c3a72;
    --sky: #1b95dc;
    --sky-light: #3ab3ee;
    --band: #17a9e8;
    --photo-light: #d9dcdf;
    --photo-dark: #6f7377;
    --white: #ffffff;
    --ink: #0a2a4f;
  }
  html, body {
    margin: 0;
    width: 1200px;
    height: 911px;
    overflow: hidden;
    background: var(--page-bg);
    font-family: "Montserrat", sans-serif;
  }
  .rollup {
    position: absolute;
    left: 400px;
    top: 25px;
    width: 400px;
    height: 860px;
    overflow: hidden;
    background: var(--white);
    box-shadow: 0 6px 24px rgba(10, 40, 80, 0.18);
  }
  .rollup-art {
    position: absolute;
    inset: 0;
  }
  .brand {
    position: absolute;
    left: 108px;
    top: 30px;
    display: flex;
    align-items: center;
    gap: 6px;
    color: var(--brand-dark);
    font-weight: 500;
    font-size: 22px;
    letter-spacing: 0.5px;
  }
  .brand-mark {
    width: 10px;
    height: 10px;
    background: var(--brand-dark);
  }
  .headline {
    position: absolute;
    left: 24px;
    top: 440px;
    margin: 0;
    color: var(--white);
    font-weight: 800;
    font-size: 36px;
    line-height: 0.98;
    letter-spacing: 0.5px;
  }
  .benefits {
    position: absolute;
    left: 52px;
    top: 604px;
    color: var(--white);
  }
  .benefits-title {
    margin: 0 0 10px 10px;
    font-weight: 700;
    font-size: 16px;
  }
  .benefits-list {
    list-style: none;
    margin: 0;
    padding: 0;
  }
  .benefits-list li {
    display: flex;
    align-items: center;
    gap: 8px;
    font-weight: 500;
    font-size: 13.5px;
    height: 27px;
  }
  .tick {
    width: 11px;
    height: 11px;
    flex: none;
  }
  .career-link {
    position: absolute;
    left: 0;
    right: 0;
    top: 812px;
    text-align: center;
    color: var(--ink);
    font-size: 10px;
    font-weight: 500;
  }
  .career-link strong { font-weight: 700; }
</style>
</head>
<body>
  <main class="rollup">
    <svg class="rollup-art" width="400" height="860" viewBox="0 0 400 860" aria-hidden="false">
      <defs>
        <linearGradient id="photoTone" x1="0" y1="0" x2="0" y2="1">
          <stop offset="0" stop-color="var(--photo-light)"/>
          <stop offset="0.55" stop-color="#a7abae"/>
          <stop offset="1" stop-color="var(--photo-dark)"/>
        </linearGradient>
        <linearGradient id="navyFade" x1="0" y1="0" x2="0" y2="1">
          <stop offset="0" stop-color="#0c3a72" stop-opacity="0"/>
          <stop offset="0.45" stop-color="#0c3a72" stop-opacity="0.85"/>
          <stop offset="1" stop-color="#0c3a72"/>
        </linearGradient>
        <linearGradient id="skyPanel" x1="0" y1="0" x2="1" y2="1">
          <stop offset="0" stop-color="var(--sky-light)"/>
          <stop offset="1" stop-color="var(--sky)"/>
        </linearGradient>
      </defs>

      <g role="img" aria-label="Schwarz-weiß Foto: Team junger Kolleginnen und Kollegen bespricht sich lachend am Tisch im Büro">
        <rect x="0" y="60" width="400" height="560" fill="url(#photoTone)"/>
      </g>

      <rect x="0" y="380" width="400" height="300" fill="url(#navyFade)"/>

      <polygon points="0,0 112,0 72,100 0,150" fill="var(--brand-dark)"/>
      <polygon points="0,0 70,0 30,80 0,130" fill="var(--sky)"/>
      <polygon points="30,80 72,100 0,150 0,130" fill="#1570b8"/>

      <polygon points="0,560 400,400 400,860 0,860" fill="var(--navy)"/>
      <polygon points="60,610 400,430 400,860 0,860 0,700" fill="url(#skyPanel)"/>
      <polygon points="250,860 400,560 400,860" fill="var(--brand-dark)"/>
      <polygon points="330,860 400,700 400,860" fill="#0a3f74"/>

      <rect x="0" y="798" width="400" height="62" fill="var(--band)"/>
    </svg>

    <div class="brand"><span class="brand-mark"></span>velmarok</div>

    <h1 class="headline">WIR<br>STELLEN<br>EIN!</h1>

    <section class="benefits">
      <h2 class="benefits-title">UNSERE ARBEITSVORTEILE:</h2>
      <ul class="benefits-list">
        <li><svg class="tick" viewBox="0 0 12 12"><rect x="0.7" y="0.7" width="10.6" height="10.6" rx="2" fill="none" stroke="#fff" stroke-width="1.2"/><path d="M3 6.2 5.2 8.3 9.2 3.6" fill="none" stroke="#fff" stroke-width="1.5"/></svg>Bis zu 100% Homeoffice möglich</li>
        <li><svg class="tick" viewBox="0 0 12 12"><rect x="0.7" y="0.7" width="10.6" height="10.6" rx="2" fill="none" stroke="#fff" stroke-width="1.2"/><path d="M3 6.2 5.2 8.3 9.2 3.6" fill="none" stroke="#fff" stroke-width="1.5"/></svg>Essenszuschuss</li>
        <li><svg class="tick" viewBox="0 0 12 12"><rect x="0.7" y="0.7" width="10.6" height="10.6" rx="2" fill="none" stroke="#fff" stroke-width="1.2"/><path d="M3 6.2 5.2 8.3 9.2 3.6" fill="none" stroke="#fff" stroke-width="1.5"/></svg>Öffi-Ticket</li>
        <li><svg class="tick" viewBox="0 0 12 12"><rect x="0.7" y="0.7" width="10.6" height="10.6" rx="2" fill="none" stroke="#fff" stroke-width="1.2"/><path d="M3 6.2 5.2 8.3 9.2 3.6" fill="none" stroke="#fff" stroke-width="1.5"/></svg>Weiterbildungen</li>
        <li><svg class="tick" viewBox="0 0 12 12"><rect x="0.7" y="0.7" width="10.6" height="10.6" rx="2" fill="none" stroke="#fff" stroke-width="1.2"/><path d="M3 6.2 5.2 8.3 9.2 3.6" fill="none" stroke="#fff" stroke-width="1.5"/></svg>Gleitzeit und vieles mehr</li>
      </ul>
    </section>

    <p class="career-link"><strong>Stellenangebote:</strong> https://www.velmarok-it.com/de/career/joboffers/</p>
  </main>
</body>
</html>
```